LunaGowns.com Banner AD

We are looking for some talented creators to create for us a banner ad for our online clothing store that specializes in dresses. We are looking for a fresh, clean, and sleek KORA, P&Q, and Glint appeal- clean, modern and sophisticated.

We would like for the final project to appear professionally done, we've had projects completed by several talent out there that did not capture our image, and let's just say it was too cluttered and appeared as if a high school editor had completed it.

I have attached a few files for you to reference, I have File 1, 2, 3, 8 and the P&Q photos as examples of what we DO like.

I have attached File 5, which is the work of one the designers that was working on this project. Although it is very simple and gets the point across, it doesn't come across like a magazine editorial.

I have attached File 6, that is the main photo we wish to use for our banner.

I have attached File 7, which is what a creator had done for us via Brevora.com, that is a good example of what we do NOT want.

That is about sums it up! I hope the examples are useful tools for you!

Hi Designers!

Thank you so much for your submissions! I enjoy viewing each and every one of them! Please view my update on what I am looking for, I have made some adjustments and have added a few more examples to reference, I have made my direction a bit more clearer. Because it seems some designers are not quite understanding my direction. I know you all have amazing talent and I am hoping to see something I am looking for and I love soon! If you have any other questions, please don't hesitate to ask! 

Target Market(s)

Our company targets women of all ages, we carry dresses that cater to every occasion, whether its an older woman looking for a dress to attend a wedding or a teenager looking for a prom dress. We want our front page banner to appear fresh, clean, with a feminine touch, we want to stray from tacky (gradients, etc..) and keep it classy all while maintaining that magazine editorial element, we want to be more fashion focused, like Glint. We want this project to appear professionally done. Our desired concept is something out of a magazine editorial, not too much going on, while shifting focus more on the dress itself than a design element like flowers or spring backgrounds.

Industry/Entity Type

High School

Requirements
Must have
• We want a glint fashion appeal, magazine editorial type of look. The phrases below should be included"

"New Season New Sexy Dresses"

"Free U.S shipping on orders $75+"
"Shop our sales up to 60% off"

All of the other phrases do not need to be included. Also, Do not include the parenthesis.
Should not have
• Only include the photo I've attached that appears solo. Please do not include the other 3 dresses that is displayed in a banner that was created for us by another designer. (that is provided as an example only)

```html
<!DOCTYPE html>
<html lang="en">
<head>
<meta charset="utf-8">
<title>LunaGowns.com — New Season Banner</title>
<link href="https://fonts.googleapis.com/css2?family=Italiana&family=Nothing+You+Could+Do&display=swap" rel="stylesheet">
<style>
  :root {
    --bg-light: #ffffff;
    --bg-shade: #e4e4e6;
    --ink: #2b2b2e;
    --slate: #4d5a70;
    --blue: #5a86c6;
    --green: #8fcf98;
    --yellow: #e9e03a;
    --red: #e4574f;
    --pink: #f08fbf;
    --lilac: #d59be0;
    --ribbon: #101816;
    --ribbon-fold: #000000;
    --sale: #e3df79;
    --rule: #c9c9cc;
    --photo-dark: #2f3a52;
    --photo-warm: #c9a184;
    --photo-mid: #8aa0b8;
  }
  * { margin: 0; padding: 0; box-sizing: border-box; }
  html, body { width: 1200px; height: 1043px; overflow: hidden; }
  body { font-family: "Italiana", serif; }

  .banner {
    position: relative;
    width: 1200px;
    height: 1043px;
    overflow: hidden;
    background: radial-gradient(ellipse at 70% 40%, var(--bg-light) 0%, #f4f4f5 45%, var(--bg-shade) 100%);
  }

  .hero-photo {
    position: absolute;
    left: 0; top: 0;
    width: 590px; height: 1043px;
    background:
      radial-gradient(ellipse 30% 18% at 55% 14%, var(--photo-warm) 0%, rgba(201,161,132,0) 100%),
      linear-gradient(180deg, rgba(228,228,230,0) 0%, rgba(138,160,184,0.35) 40%, var(--photo-dark) 100%),
      linear-gradient(90deg, #dcdcde 0%, var(--photo-mid) 50%, #dcdcde 100%);
  }

  .slider-arrow { position: absolute; left: 14px; top: 300px; }

  .copy {
    position: absolute;
    left: 598px; width: 402px; top: 0;
    text-align: center;
  }

  .season-title {
    margin-top: 52px;
    font-weight: 400;
    font-size: 86px;
    line-height: 80px;
    letter-spacing: 2px;
    color: var(--slate);
  }
  .season-title .c-slate { color: var(--slate); }
  .season-title .c-blue { color: var(--blue); }
  .season-title .c-green { color: var(--green); }
  .season-title .c-yellow { color: var(--yellow); }
  .season-title .c-red { color: var(--red); }
  .season-title .c-pink { color: var(--pink); }
  .season-title .c-lilac { color: var(--lilac); }

  .title-rule {
    width: 402px; height: 1px;
    margin: 38px auto 0;
    background: linear-gradient(90deg, rgba(0,0,0,0), #8d8d90 50%, rgba(0,0,0,0));
  }

  .collection-title {
    margin-top: 44px;
    font-weight: 400;
    font-size: 70px;
    line-height: 66px;
    color: var(--ink);
    letter-spacing: 1px;
  }

  .sale-ribbon {
    position: relative;
    margin: 82px auto 0;
    width: 394px; height: 100px;
  }
  .sale-ribbon svg { position: absolute; left: 0; top: 0; }
  .sale-label {
    position: absolute; left: 0; right: 0; top: 12px;
    font-size: 70px; line-height: 70px;
    color: var(--sale);
    letter-spacing: 1px;
  }

  .offer {
    font-family: "Nothing You Could Do", cursive;
    color: var(--ink);
    font-size: 38px;
    line-height: 46px;
    transform: rotate(-5deg);
  }
  .offer-sale { margin-top: 52px; }
  .offer-rule {
    width: 290px; height: 1px;
    margin: 26px auto 0;
    background: linear-gradient(90deg, rgba(0,0,0,0), var(--rule) 50%, rgba(0,0,0,0));
    transform: rotate(-5deg);
  }
  .offer-shipping { margin-top: 34px; }
</style>
</head>
<body>
<main class="banner">
  <div class="hero-photo" role="img" aria-label="Model with long wavy blonde hair, seen from behind and smiling over her shoulder, wearing a fitted open-back dark dress with bright tropical floral print"></div>

  <svg class="slider-arrow" width="16" height="40" viewBox="0 0 16 40" aria-hidden="true">
    <polygon points="16,0 0,20 16,40" fill="#ffffff"/>
  </svg>

  <section class="copy">
    <h1 class="season-title">
      <span class="c-slate">N</span><span class="c-blue">E</span><span class="c-slate">W</span><br>
      <span class="c-green">S</span><span class="c-yellow">E</span><span class="c-red">A</span><span class="c-pink">S</span><span class="c-lilac">O</span><span class="c-slate">N</span>
    </h1>
    <div class="title-rule"></div>
    <h2 class="collection-title">NEW<br>SEXY<br>DRESSES</h2>

    <div class="sale-ribbon">
      <svg width="394" height="100" viewBox="0 0 394 100" aria-hidden="true">
        <polygon points="0,18 34,18 34,100 0,100 16,59" fill="var(--ribbon-fold)"/>
        <polygon points="394,0 360,0 360,82 394,82 378,41" fill="var(--ribbon-fold)"/>
        <polygon points="20,8 374,0 374,84 20,92" fill="var(--ribbon)"/>
      </svg>
      <div class="sale-label">SALE%</div>
    </div>

    <p class="offer offer-sale">Shop our sales<br>up to 60% off</p>
    <div class="offer-rule"></div>
    <p class="offer offer-shipping">Free U.S shipping<br>on orders $75+</p>
  </section>
</main>
</body>
</html>
```